Crestwell Advisory Services

I'm looking to create a flyer for my business to provide a consultant service. I will be providing the following below
Launch Your Business Today for only $150
(state fee not included)
Business Formation includes:
*Limited liability Corporation (LLC)
*Halvers and Quint Number
*FEIN
*Operation Agreement for partnership LLCs (For 2 or more member(s)
*Commercial Activity license (If needed for your Business )
*Same -day turnaround service with documents
Schedule your Appointment today
Call or text:318-472-6051
Email:MoralesCapitalCircle@fernmail.net
Target Market(s)
I want the flyer to attract people who wants to start a business but doesn’t know where to start. I want the flyer to stand out form the other consultant businesses.
Industry/Entity Type
Consultant
Requirements
Must have
- The State fee not included should be in small print
Highlight the price or service
Highlight the phrase "launch you business today"
Nice to have
- Different samples of colors, a variety
Should not have
- should not be all one color

```html
<!DOCTYPE html>
<html lang="en">
<head>
<meta charset="utf-8">
<title>Morales Capital Circle – Business Formation Flyer</title>
<link rel="stylesheet" href="https://fonts.googleapis.com/css2?family=Cinzel:wght@400&family=Bebas+Neue&family=Cabin:wght@400;600;700&display=swap">
<style>
  :root {
    --navy: #1b2a4e;
    --navy-deep: #142140;
    --orange: #f07126;
    --teal: #17a58f;
    --paper: #ffffff;
    --mist: #eef0f2;
    --ink: #1d2233;
    --stage: #e4e5e7;
  }
  * { margin: 0; padding: 0; box-sizing: border-box; }
  html, body { width: 1200px; height: 807px; overflow: hidden; background: var(--stage); }
  body { position: relative; font-family: "Cabin", Arial, sans-serif; color: var(--ink); }

  .flyer {
    position: absolute; left: 294px; top: 7px;
    width: 612px; height: 792px;
    background: var(--paper); overflow: hidden;
    box-shadow: 0 2px 10px rgba(0,0,0,.18);
  }

  .masthead {
    position: absolute; left: 0; top: 0; width: 612px; height: 106px;
    text-align: center; padding-top: 22px;
    font-family: "Cinzel", Georgia, serif; font-size: 25px; line-height: 33px;
    color: var(--navy); letter-spacing: .5px;
  }
  .masthead-notch { position: absolute; left: 274px; top: 106px; z-index: 2; }

  .hero {
    position: absolute; left: 0; top: 106px; width: 612px; height: 290px;
    background: var(--navy);
    text-align: center;
  }
  .hero-backdrop {
    position: absolute; inset: 0;
    background: linear-gradient(160deg, #223563 0%, #1b2a4e 45%, #2a3d6a 80%, #22345d 100%);
  }
  .hero-title {
    position: relative; padding-top: 84px;
    font-family: "Bebas Neue", Impact, sans-serif; font-size: 47px; line-height: 48px;
    color: #fff; letter-spacing: 1px;
  }
  .price-tag {
    position: relative; display: inline-block; margin-top: 12px;
    background: var(--orange); color: #fff;
    font-family: "Bebas Neue", Impact, sans-serif; font-size: 41px; line-height: 45px;
    padding: 0 26px; letter-spacing: 1px; border-radius: 2px;
  }
  .fine-print { position: relative; margin-top: 14px; font-size: 13px; color: #d9dded; }

  .gap { position: absolute; left: 0; top: 396px; width: 612px; height: 15px; background: var(--mist); }

  .prompt-band {
    position: absolute; left: 0; top: 411px; width: 612px; height: 67px;
    background: var(--orange); color: #fff;
    font-weight: 700; font-size: 16px; text-transform: uppercase;
  }
  .prompt-band span { position: absolute; top: 23px; }
  .prompt-question { left: 27px; }
  .prompt-provider { left: 330px; }
  .prompt-divider { position: absolute; left: 302px; top: 15px; width: 2px; height: 37px; background: #fff; opacity: .9; }

  .includes {
    position: absolute; left: 0; top: 478px; width: 612px; height: 255px;
    background: linear-gradient(180deg, #f1f3f5, #e9ecef);
  }
  .includes-card {
    position: absolute; left: 18px; top: 38px; width: 580px; height: 196px;
    background: var(--paper); border-radius: 3px;
  }
  .includes-tab { position: absolute; left: 10px; top: 23px; }
  .includes-tab-label {
    position: absolute; left: 27px; top: 29px;
    color: #fff; font-weight: 700; font-size: 15px; text-transform: uppercase;
  }
  .service { position: absolute; display: flex; align-items: center; gap: 6px; font-size: 13px; line-height: 14px; }
  .service svg { flex: none; }

  .contact-bar { position: absolute; left: 0; top: 733px; width: 612px; height: 59px; background: var(--navy-deep); }
  .contact-shapes { position: absolute; left: 0; top: 0; }
  .contact-schedule { position: absolute; left: 17px; top: 14px; color: #fff; font-size: 12px; font-weight: 600; text-transform: uppercase; }
  .contact-phone { position: absolute; left: 17px; top: 33px; color: #fff; font-size: 12px; display: flex; align-items: center; gap: 5px; }
  .contact-phone b { font-weight: 700; }
  .contact-email { position: absolute; left: 348px; top: 26px; color: #fff; font-size: 11px; display: flex; align-items: center; gap: 5px; }
  .contact-phone svg, .contact-email svg { flex: none; }
</style>
</head>
<body>
<main class="flyer">
  <header class="masthead">MORALES<br>CAPITAL CIRCLE</header>
  <svg class="masthead-notch" width="64" height="16" viewBox="0 0 64 16"><polygon points="0,0 64,0 32,16" fill="#ffffff"/></svg>

  <section class="hero">
    <div class="hero-backdrop" role="img" aria-label="Faded photograph of office towers seen from below, in navy tones"></div>
    <h1 class="hero-title">LAUNCH YOUR BUSINESS TODAY</h1>
    <div class="price-tag">FOR ONLY $150</div>
    <p class="fine-print">(state fee not included)</p>
  </section>

  <div class="gap"></div>

  <section class="prompt-band">
    <span class="prompt-question">Don’t know where to start?</span>
    <div class="prompt-divider"></div>
    <span class="prompt-provider">Crestwell Advisory Services</span>
  </section>

  <section class="includes">
    <div class="includes-card"></div>
    <svg class="includes-tab" width="316" height="29" viewBox="0 0 316 29">
      <polygon points="0,0 302,0 316,29 8,29 0,22" fill="#17a58f"/>
    </svg>
    <span class="includes-tab-label">Business formation includes:</span>

    <div class="service" style="left:25px;top:70px;">
      <svg width="48" height="44" viewBox="0 0 48 44"><polygon points="12,2 36,2 46,22 36,42 12,42 2,22" fill="none" stroke="#1b2a4e" stroke-width="1.4"/><circle cx="18" cy="16" r="3" fill="#17a58f"/><circle cx="30" cy="16" r="3" fill="#17a58f"/><rect x="14" y="21" width="20" height="11" fill="#1b2a4e"/></svg>
      <span>Limited liability Corporation (LLC)</span>
    </div>
    <div class="service" style="left:25px;top:118px;">
      <svg width="48" height="44" viewBox="0 0 48 44"><polygon points="12,2 36,2 46,22 36,42 12,42 2,22" fill="none" stroke="#1b2a4e" stroke-width="1.4"/><circle cx="24" cy="20" r="6" fill="#17a58f"/><rect x="21" y="26" width="6" height="5" fill="#1b2a4e"/></svg>
      <span>Halvers and Quint Number</span>
    </div>
    <div class="service" style="left:25px;top:166px;">
      <svg width="48" height="44" viewBox="0 0 48 44"><polygon points="12,2 36,2 46,22 36,42 12,42 2,22" fill="none" stroke="#1b2a4e" stroke-width="1.4"/><rect x="24" y="11" width="10" height="14" fill="#17a58f"/><circle cx="20" cy="25" r="5" fill="none" stroke="#1b2a4e" stroke-width="2"/><line x1="16" y1="29" x2="12" y2="33" stroke="#1b2a4e" stroke-width="2.5"/></svg>
      <span>FEIN</span>
    </div>

    <div class="service" style="left:303px;top:70px;">
      <svg width="48" height="44" viewBox="0 0 48 44"><polygon points="12,2 36,2 46,22 36,42 12,42 2,22" fill="none" stroke="#1b2a4e" stroke-width="1.4"/><circle cx="16" cy="18" r="3" fill="#17a58f"/><circle cx="24" cy="15" r="3.5" fill="#1b2a4e"/><circle cx="32" cy="18" r="3" fill="#17a58f"/><rect x="12" y="23" width="24" height="7" rx="3" fill="#1b2a4e"/></svg>
      <span>Operation Agreement for partnership<br>LLCs (For 2 or more member(s)</span>
    </div>
    <div class="service" style="left:303px;top:118px;">
      <svg width="48" height="44" viewBox="0 0 48 44"><polygon points="12,2 36,2 46,22 36,42 12,42 2,22" fill="none" stroke="#1b2a4e" stroke-width="1.4"/><rect x="15" y="11" width="15" height="20" fill="none" stroke="#1b2a4e" stroke-width="1.6"/><line x1="18" y1="17" x2="27" y2="17" stroke="#17a58f" stroke-width="2"/><line x1="18" y1="22" x2="27" y2="22" stroke="#17a58f" stroke-width="2"/><line x1="34" y1="13" x2="27" y2="30" stroke="#1b2a4e" stroke-width="2"/></svg>
      <span>Commercial Activity license<br>(If needed for your Business )</span>
    </div>
    <div class="service" style="left:303px;top:166px;">
      <svg width="48" height="44" viewBox="0 0 48 44"><polygon points="12,2 36,2 46,22 36,42 12,42 2,22" fill="none" stroke="#1b2a4e" stroke-width="1.4"/><circle cx="24" cy="22" r="9" fill="none" stroke="#17a58f" stroke-width="2" stroke-dasharray="40 8"/><polyline points="24,16 24,22 28,25" fill="none" stroke="#1b2a4e" stroke-width="2"/></svg>
      <span>Same -day turnaround service<br>with documents</span>
    </div>
  </section>

  <footer class="contact-bar">
    <svg class="contact-shapes" width="612" height="59" viewBox="0 0 612 59">
      <polygon points="0,0 266,0 288,59 0,59" fill="#1b2a4e"/>
      <polygon points="272,20 612,20 612,46 282,46" fill="#f07126"/>
    </svg>
    <span class="contact-schedule">Schedule your appointment today</span>
    <span class="contact-phone">Call or text:
      <svg width="12" height="14" viewBox="0 0 12 14"><rect x="2.5" y="1" width="7" height="12" rx="1.5" fill="none" stroke="#fff" stroke-width="1.4"/><circle cx="6" cy="11" r=".8" fill="#fff"/></svg>
      <b>318-472-6051</b></span>
    <span class="contact-email">
      <svg width="11" height="11" viewBox="0 0 11 11"><circle cx="5.5" cy="5.5" r="5.5" fill="#fff"/><rect x="2.5" y="3.5" width="6" height="4" fill="#f07126"/></svg>
      MoralesCapitalCircle@fernmail.net</span>
  </footer>
</main>
</body>
</html>
```